POP/ROCK artist: CD Cover Design Project

IF U LOVE MUSIC AND ALBUM COVER ART THEN PLEASE PARTICIPATE IN MY PROJECT AND HAVE A GREAT TIME DESIGNING SOMETHING UNIQUE AND EXCITING!!!!
Hi, my name is tovo, a pop/rock artist living in Europe. i just finished recording a fun dance song, called SPINNIN WILD HEARTS, with a successful Brightfield Records producer in Europe and I just put the finishing touches on the music video shot in LA. Now i'm going to release the song and video with PulsaWave. It's going to go out to about 750 stores, including SongCrate, tunebox and all the other biggies as well as a load of smaller ones.
I need a great looking CD cover design that i can plaster everywhere . . . and i really mean everywhere i can.
As per PulsaWave' specs, the cover art MUST BE 1500 x 1500 pixels. It cannot be blurry or pixilated and must be perfectly square.
I've uploaded some pics for you to choose from but you can use whichever one(s) you like . . . or none of them if you prefer, according to your inspiration. Just let me know if you want other pics and i can upload others.
Updates
Hey there,
Hey there,
Hi again, all,
Hey there,
Hi there, designers!
Hello everybody,
Target Market(s)
Modern pop/rock radio listeners of Kestrel Radio, ZPX, etc.
Please click on the following link to see the music video and hear the song:
http://www.clipvault.example/watch?v=Qr7tLm2Wd9a
Also, i have various pics and photos i can upload . . . just tell me what you need!!!!!
Requirements
Must have
- As per PulsaWave' specs, the cover art MUST BE 1500 x 1500 pixels. It cannot be blurry or pixilated and must be perfectly square.
My artist name, tovo, and the song title, Spinnin Wild Hearts, must be on the cover art.
The destination for your design is online music stores like SongCrate. So the dimensions will be VERY SMALL The actual size seen by the public will be about 1.5 cm x 1.5 cm! (Please have a look at the SongCrate store to see the actual size people will view the designs in.)
This means that your designs have to be clearly communicated at that size. The title of the song (spinnin wild hearts) and my artist name (tovo) have to be large enough to read and whatever idea you're going for has to be easily understood.
Nice to have
- It should look totally modern and pop/rock, hip and cool. It's up to you and your design magic to do whatever you think it takes.
Should not have
- Website and e-mail addresses CANNOT be included anywhere on cover art.

```html
<!DOCTYPE html>
<html lang="en">
<head>
<meta charset="utf-8">
<title>tovo — Spinnin Wild Hearts</title>
<link rel="stylesheet" href="https://fonts.googleapis.com/css2?family=Archivo+Black&family=Squada+One&display=swap">
<style>
  :root {
    --lime: #d6ff00;
    --paper: #ffffff;
    --ink: #050505;
    --photo-dark: #1a1a1a;
    --photo-mid: #5a5a5a;
  }
  html, body {
    margin: 0;
    padding: 0;
    width: 1200px;
    height: 1200px;
    overflow: hidden;
    background: var(--lime);
  }
  .cover {
    display: block;
    width: 1200px;
    height: 1200px;
  }
  .cover-bg { fill: var(--lime); }
  .artist-name {
    font-family: "Archivo Black", "Arial Black", sans-serif;
    font-size: 520px;
    fill: var(--paper);
    letter-spacing: -8px;
  }
  .song-title {
    font-family: "Squada One", "Impact", sans-serif;
    font-size: 122px;
    fill: var(--ink);
  }
</style>
</head>
<body>
<svg class="cover" viewBox="0 0 1200 1200" xmlns="http://www.w3.org/2000/svg">
  <defs>
    <linearGradient id="photoTone" x1="0" y1="0" x2="0" y2="1">
      <stop offset="0" stop-color="var(--photo-dark)"/>
      <stop offset="0.65" stop-color="var(--photo-dark)"/>
      <stop offset="1" stop-color="var(--photo-mid)"/>
    </linearGradient>
  </defs>

  <rect class="cover-bg" x="0" y="0" width="1200" height="1200"/>

  <rect class="artist-photo" role="img"
        aria-label="Upside-down photo of the guitarist in a dark suit and sunglasses playing a white electric guitar, with motion blur"
        x="100" y="0" width="770" height="800" fill="url(#photoTone)"/>

  <text class="artist-name" x="-10" y="1028">tovo</text>

  <text class="song-title" x="12" y="1118" textLength="990" lengthAdjust="spacingAndGlyphs">SPINNIN WILD HEARTS</text>
</svg>
</body>
</html>
```